Lumo Care — Premium Telehealth Marketing Website

Lumo Care is a modern, cash-pay telehealth brand offering prescription weight-loss (GLP-1) and sexual-health treatment online, with licensed US providers — no insurance required. We're building a premium, trustworthy direct-to-consumer healthcare brand in the same tier as Welk, Tu, and Orla.

We need a clean, modern, premium marketing website design — warm and trustworthy, not cold or clinical. Think high-end wellness brand: generous whitespace, elegant typography, calm and confident. It should feel medically credible but human and approachable.

WHAT WE NEED DESIGNED (3 core templates that define the whole site):

1. Homepage — the brand showcase that establishes the full visual language (hero, sections, product highlights, how-it-works, trust elements, footer).

2. Product / Treatment page template — a reusable layout for any medication (transparent pricing, how it works, what's included, clinical info, safety, clear call-to-action). We'll reuse this pattern for all treatments.

3. Interior / Content page template — a flexible layout for sub-pages like How It Works, About, Contact, FAQ, and legal pages.

We'll implement the final site ourselves in React/Next.js + Tailwind CSS, so clean, well-structured design (and HTML/CSS if you provide it) is a strong plus.

BRAND DIRECTION (already established — please design within this):

- Logo: lowercase wordmark "lumo." with the period in gold (see attached). Please build the design around this existing logo.
- Colors: deep navy (#0B1B33 and #14315C) with a warm gold accent (#E0A458); soft light backgrounds (#EEF3F9, #FBFCFE).
- Typography: a refined serif for headlines (e.g., Fraunces) paired with a clean sans-serif for body (e.g., Inter).
- Tone: premium, warm, trustworthy, human.

INSPIRATION / QUALITY BAR: Welk (welk.example), Tu (tu.example), Orla — the polished DTC healthcare aesthetic. We want that tier of quality, with our own warmer navy-and-gold identity.

Industry/Entity Type

Telemedicine

Coding

Coded - Design and coding required

Number of Pages Required

3 page

Requirements
Nice to have
• Side Scrolling Medictions bar like on Tu.example

```html
<!DOCTYPE html>
<html lang="en">
<head>
<meta charset="utf-8">
<title>Lumo Care — Site Templates</title>
<link href="https://fonts.googleapis.com/css2?family=Fraunces:opsz,wght@9..144,300;9..144,400&family=Inter:wght@400;500;600;700&display=swap" rel="stylesheet">
<style>
:root{
  --navy:#0B1B33;
  --navy-2:#14315C;
  --gold:#E0A458;
  --bg-soft:#EEF3F9;
  --bg-page:#F5F8FC;
  --white:#FBFCFE;
  --text:#3c4a5e;
  --muted:#8a95a5;
  --line:#dfe5ee;
  --serif:'Fraunces', Georgia, serif;
  --sans:'Inter', Arial, sans-serif;
}
*{box-sizing:border-box;margin:0;padding:0}
html,body{width:1200px;height:1200px;overflow:hidden;background:#fff}
body{position:relative;font-family:var(--sans);color:var(--navy)}
.page{position:absolute;top:0;overflow:hidden}
.abs{position:absolute}
.serif{font-family:var(--serif);font-weight:300;color:var(--navy)}
.nav{position:absolute;left:0;top:0;right:0;background:#fff}
.logo{position:absolute;font-family:var(--serif);font-weight:400;color:var(--navy);background:var(--bg-soft);padding:0 2px;line-height:1.3}
.nav-link{position:absolute;font-size:3.6px;color:var(--navy)}
.nav-link.active{color:var(--gold)}
.pill-btn{position:absolute;background:var(--navy);color:#fff;border-radius:20px;font-weight:600;display:flex;align-items:center;justify-content:center;text-align:center}
.ghost-btn{position:absolute;border:1px solid var(--navy);color:var(--navy);border-radius:20px;font-weight:600;display:flex;align-items:center;justify-content:center;background:#fff}
.photo{position:absolute;border-radius:6px}
.small{font-size:3.4px;line-height:1.55;color:var(--text)}
.card{position:absolute;background:#fff;border-radius:5px;box-shadow:0 2px 8px rgba(11,27,51,.06)}
.eyebrow{font-size:2.6px;letter-spacing:.3px;color:var(--gold);text-transform:uppercase;font-weight:600}
.footer{position:absolute;left:0;right:0;background:var(--navy);color:#c9d3e2}
.f-logo{position:absolute;font-family:var(--serif);font-weight:400;color:var(--gold)}
.f-head{position:absolute;font-size:3.4px;font-weight:700;letter-spacing:.3px;color:#fff}
.f-link{position:absolute;font-size:3.3px;color:#c9d3e2}
.f-rule{position:absolute;height:1px;background:rgba(255,255,255,.12)}
.tick{display:inline-block;width:4px;height:4px;vertical-align:middle;margin-right:3px}
.faq-row{position:absolute;border-top:1px solid var(--line);display:flex;align-items:center;justify-content:space-between;font-size:3.6px;color:var(--navy)}
.chev{width:3px;height:3px;border-right:.6px solid var(--muted);border-bottom:.6px solid var(--muted);transform:rotate(45deg);margin-right:3px}
.badge{position:absolute;background:rgba(255,255,255,.92);border-radius:6px;font-size:2.5px;color:var(--navy);padding:1px 3px;display:flex;align-items:center;gap:2px}
.badge i{width:3px;height:3px;border-radius:50%;border:.5px solid var(--gold);display:inline-block}
</style>
</head>
<body>

<!-- ============ HOMEPAGE ============ -->
<section class="page home" style="left:0;width:360px;height:1200px;background:var(--bg-soft)">
  <div class="nav" style="height:16px">
    <div class="logo" style="left:42px;top:5px;font-size:5px">lumo.</div>
    <div class="nav-link" style="left:121px;top:6px;font-size:3px">Treatments</div>
    <div class="nav-link" style="left:146px;top:6px;font-size:3px">How it Works</div>
    <div class="nav-link" style="left:175px;top:6px;font-size:3px">About Us</div>
    <div class="nav-link" style="left:197px;top:6px;font-size:3px">Contact</div>
    <div class="nav-link" style="left:275px;top:6px;font-size:3px">Log In</div>
    <div class="pill-btn" style="left:290px;top:4px;width:29px;height:8px;font-size:2.8px">Get Started</div>
  </div>

  <div class="abs serif" style="left:42px;top:60px;font-size:13.5px;line-height:1.25;width:130px">Healthcare that fits your life.</div>
  <p class="abs small" style="left:42px;top:99px;width:135px;font-size:3.6px">Prescription weight-loss and sexual-health treatments online, with licensed providers and transparent pricing. No insurance required.</p>
  <div class="pill-btn" style="left:42px;top:129px;width:33px;height:18px;font-size:3.4px;line-height:1.1">Get<br>Started</div>
  <div class="ghost-btn" style="left:79px;top:129px;width:50px;height:13px;font-size:3.4px">See Treatments</div>

  <div class="photo" role="img" aria-label="Woman smiling on a sofa with a laptop in a sunlit living room" style="left:187px;top:36px;width:132px;height:153px;background:linear-gradient(160deg,#d8c5a8,#b99a74 55%,#e7dccb);border-radius:6px 6px 0 0"></div>
  <div class="badge" style="left:274px;top:47px"><i></i>Licensed U.S. Providers</div>
  <div class="badge" style="left:187px;top:66px"><i></i>Secure Telehealth</div>
  <div class="badge" style="left:280px;top:136px"><i></i>Transparent Pricing</div>
  <div class="badge" style="left:187px;top:154px"><i></i>Discreet Shipping</div>
  <div class="badge" style="left:187px;top:178px"><i></i>Discreet Shipping</div>

  <div class="abs" style="left:0;top:189px;width:360px;height:14px;background:var(--navy);color:var(--gold);font-family:var(--serif);font-size:4px;letter-spacing:.6px;white-space:nowrap;display:flex;align-items:center;gap:9px;padding-left:7px">
    <span>GLP-1 WEIGHT LOSS</span><span>•</span><span>ED TREATMENTS</span><span>•</span><span>HAIR LOSS PREVENTION</span><span>•</span><span>MENTAL HEALTH SUPPORT</span><span>•</span><span>TESTOSTERONE SUPPORT</span>
  </div>

  <div class="abs serif" style="left:0;width:360px;top:226px;text-align:center;font-size:10.5px">Simple. Private. Effective.</div>
  <div class="abs" style="left:129px;top:273px;width:102px;height:1px;background:#ead7b9"></div>
  <div class="card" style="left:42px;top:257px;width:87px;height:58px;padding:20px 9px 0">
    <div class="serif" style="font-size:4.6px;font-weight:400">Choose Treatment</div>
    <p class="small" style="font-size:3px;margin-top:3px">Answer a few questions about your health history and goals online in under 5 minutes.</p>
  </div>
  <div class="card" style="left:136px;top:257px;width:88px;height:58px;padding:20px 9px 0">
    <div class="serif" style="font-size:4.6px;font-weight:400">Medical Review</div>
    <p class="small" style="font-size:3px;margin-top:3px">A licensed U.S. provider will review your answers and prescribe treatment if appropriate.</p>
  </div>
  <div class="card" style="left:231px;top:257px;width:88px;height:58px;padding:20px 9px 0">
    <div class="serif" style="font-size:4.6px;font-weight:400">Delivered To Your Door</div>
    <p class="small" style="font-size:3px;margin-top:3px">Your medication is shipped fast and free in discreet, unbranded packaging.</p>
  </div>

  <div class="abs" style="left:0;top:338px;width:360px;height:189px;background:var(--white)"></div>
  <div class="abs serif" style="left:0;width:360px;top:360px;text-align:center;font-size:10.5px">Treatments tailored to you</div>
  <div class="abs small" style="left:0;width:360px;top:381px;text-align:center;font-size:3.4px">Clinically-proven solutions for a healthier life.</div>

  <div class="card" style="left:42px;top:389px;width:87px;height:115px">
    <div role="img" aria-label="Woman jogging on a park trail" style="height:53px;border-radius:5px 5px 0 0;background:linear-gradient(180deg,#9dbbd0,#6f8f5a 55%,#4d6a3c)"></div>
    <div style="padding:8px 7px 0"><div class="eyebrow">Weight Loss</div>
    <div class="serif" style="font-size:5.2px;font-weight:400;margin-top:3px">GLP-1 Programs</div>
    <p class="small" style="font-size:3px;margin-top:3px">Sustainable weight loss with medical support and prescription treatments.</p></div>
    <div class="ghost-btn" style="left:7px;top:96px;width:73px;height:10px;font-size:3px">Learn More</div>
  </div>
  <div class="card" style="left:136px;top:389px;width:88px;height:115px">
    <div role="img" aria-label="Black and white portrait in soft light" style="height:53px;border-radius:5px 5px 0 0;background:linear-gradient(180deg,#5a5a5a,#2a2a2a)"></div>
    <div style="padding:8px 7px 0"><div class="eyebrow">Sexual Health</div>
    <div class="serif" style="font-size:5.2px;font-weight:400;margin-top:3px">ED &amp; Performance</div>
    <p class="small" style="font-size:3px;margin-top:3px">Effective, discreet treatments to help you perform your best when it matters.</p></div>
    <div class="ghost-btn" style="left:7px;top:96px;width:74px;height:10px;font-size:3px">Learn More</div>
  </div>
  <div class="card" style="left:231px;top:389px;width:88px;height:115px">
    <div role="img" aria-label="Silhouette doing yoga at sunset by the sea" style="height:53px;border-radius:5px 5px 0 0;background:linear-gradient(180deg,#6d6f8e,#c49aa6 60%,#e8b6a2)"></div>
    <div style="padding:8px 7px 0"><div class="eyebrow">Men's Health</div>
    <div class="serif" style="font-size:5.2px;font-weight:400;margin-top:3px">Hormone &amp; Wellness</div>
    <p class="small" style="font-size:3px;margin-top:3px">Comprehensive plans to restore energy, focus, and overall vitality.</p></div>
    <div class="ghost-btn" style="left:7px;top:96px;width:74px;height:10px;font-size:3px">Learn More</div>
  </div>

  <div class="photo" role="img" aria-label="Smiling doctor in a white coat outdoors by a tree" style="left:35px;top:555px;width:130px;height:86px;background:linear-gradient(135deg,#b9c4b0,#dfe3dc 55%,#aab49c);opacity:.85"></div>
  <div class="abs serif" style="left:196px;top:550px;width:130px;font-size:8px;line-height:1.3;color:#97a1af">Premium care, without the premium price tag.</div>
  <div class="abs small" style="left:196px;top:577px;font-size:3.2px;color:#9aa4b2;line-height:3.4">
    <div><svg class="tick" viewBox="0 0 10 10"><circle cx="5" cy="5" r="4.3" fill="none" stroke="#bfe0d0" stroke-width="1"/><path d="M3 5.2l1.4 1.4L7 3.8" fill="none" stroke="#bfe0d0" stroke-width="1"/></svg>No insurance required</div>
    <div><svg class="tick" viewBox="0 0 10 10"><circle cx="5" cy="5" r="4.3" fill="none" stroke="#bfe0d0" stroke-width="1"/><path d="M3 5.2l1.4 1.4L7 3.8" fill="none" stroke="#bfe0d0" stroke-width="1"/></svg>Transparent, upfront pricing</div>
    <div><svg class="tick" viewBox="0 0 10 10"><circle cx="5" cy="5" r="4.3" fill="none" stroke="#bfe0d0" stroke-width="1"/><path d="M3 5.2l1.4 1.4L7 3.8" fill="none" stroke="#bfe0d0" stroke-width="1"/></svg>Ongoing medical support</div>
    <div><svg class="tick" viewBox="0 0 10 10"><circle cx="5" cy="5" r="4.3" fill="none" stroke="#bfe0d0" stroke-width="1"/><path d="M3 5.2l1.4 1.4L7 3.8" fill="none" stroke="#bfe0d0" stroke-width="1"/></svg>FDA-approved treatments</div>
    <div><svg class="tick" viewBox="0 0 10 10"><circle cx="5" cy="5" r="4.3" fill="none" stroke="#bfe0d0" stroke-width="1"/><path d="M3 5.2l1.4 1.4L7 3.8" fill="none" stroke="#bfe0d0" stroke-width="1"/></svg>Fast, free shipping</div>
  </div>
  <div class="pill-btn" style="left:191px;top:638px;width:41px;height:9px;font-size:2.8px;background:var(--navy-2)">Start Your Visit</div>

  <div class="abs" style="left:0;top:671px;width:360px;height:174px;background:var(--white)"></div>
  <div class="abs serif" style="left:0;width:360px;top:692px;text-align:center;font-size:10.5px">Patient Results</div>
  <div class="card" style="left:90px;top:723px;width:180px;height:79px;text-align:center">
    <div style="color:var(--gold);font-size:5px;letter-spacing:1px;margin-top:10px">★★★★★</div>
    <p class="serif" style="font-style:italic;font-size:4.4px;line-height:1.5;padding:3px 12px 0;font-weight:300">"Lumo completely changed my life. The providers were incredibly supportive, and the medication arrived right at my door. I've lost 30lbs and kept it off!"</p>
    <div style="position:absolute;left:60px;top:52px;width:12px;height:12px;border-radius:50%;background:#d9dde3" role="img" aria-label="Patient avatar"></div>
    <div class="serif" style="position:absolute;left:78px;top:54px;font-size:3.4px;font-weight:400">Maya R.</div>
    <div style="position:absolute;left:78px;top:60px;font-size:2.4px;letter-spacing:.3px;color:var(--muted)">WEIGHT LOSS PROGRAM</div>
  </div>
  <div class="abs" style="left:160px;top:812px;width:10px;height:10px;border-radius:50%;background:#fff;box-shadow:0 1px 3px rgba(0,0,0,.1);font-size:5px;text-align:center;line-height:10px">‹</div>
  <div class="abs" style="left:175px;top:816px;width:2px;height:2px;border-radius:50%;background:var(--navy)"></div>
  <div class="abs" style="left:179px;top:816px;width:2px;height:2px;border-radius:50%;background:#c7ced8"></div>
  <div class="abs" style="left:190px;top:812px;width:10px;height:10px;border-radius:50%;background:#fff;box-shadow:0 1px 3px rgba(0,0,0,.1);font-size:5px;text-align:center;line-height:10px">›</div>

  <div class="abs serif" style="left:0;width:360px;top:866px;text-align:center;font-size:10.5px">Frequently Asked Questions</div>
  <div class="faq-row" style="left:90px;top:899px;width:180px;height:20px">Do I need insurance?<span class="chev"></span></div>
  <div class="faq-row" style="left:90px;top:919px;width:180px;height:20px">Are the healthcare providers licensed?<span class="chev"></span></div>
  <div class="faq-row" style="left:90px;top:939px;width:180px;height:20px">How does the shipping work?<span class="chev"></span></div>
  <div class="faq-row" style="left:90px;top:959px;width:180px;height:20px;border-bottom:1px solid var(--line)">What happens if I'm not eligible for treatment?<span class="chev"></span></div>

  <div class="footer" style="top:1001px;height:199px">
    <div class="abs serif" style="left:0;width:360px;top:26px;text-align:center;font-size:9.5px;color:#fff">Feel Better. Live Better.</div>
    <div class="abs" style="left:0;width:360px;top:46px;text-align:center;font-size:3.6px;color:#d3dbe7">Join thousands of patients taking control of their health.</div>
    <div class="pill-btn" style="left:147px;top:61px;width:66px;height:13px;font-size:3.4px;background:var(--gold);color:#fff">Start Your Consultation</div>
    <div class="f-logo" style="left:42px;top:119px;font-size:7px">lumo.</div>
    <div class="abs" style="left:42px;top:132px;width:70px;font-size:3.1px;line-height:1.6;color:#d3dbe7">Healthcare that fits your life. Prescription weight-loss and sexual-health treatments online.</div>
    <div class="f-head" style="left:150px;top:120px;font-size:3px">TREATMENTS</div>
    <div class="f-link" style="left:150px;top:131px;font-size:3px">Weight Loss</div>
    <div class="f-link" style="left:150px;top:140px;font-size:3px">Sexual Health</div>
    <div class="f-link" style="left:150px;top:150px;font-size:3px">Men's Health</div>
    <div class="f-head" style="left:210px;top:120px;font-size:3px">COMPANY</div>
    <div class="f-link" style="left:210px;top:131px;font-size:3px">About Us</div>
    <div class="f-link" style="left:210px;top:140px;font-size:3px">How it Works</div>
    <div class="f-link" style="left:210px;top:150px;font-size:3px">FAQ</div>
    <div class="f-link" style="left:210px;top:159px;font-size:3px">Contact</div>
    <div class="f-head" style="left:270px;top:120px;font-size:3px">LEGAL</div>
    <div class="f-link" style="left:270px;top:131px;font-size:3px">Terms of Service</div>
    <div class="f-link" style="left:270px;top:140px;font-size:3px">Privacy Policy</div>
    <div class="f-link" style="left:270px;top:150px;font-size:3px">Telehealth Consent</div>
    <div class="f-link" style="left:270px;top:159px;font-size:3px">Provider Login</div>
    <div class="f-rule" style="left:42px;width:277px;top:177px"></div>
    <div class="f-link" style="left:150px;top:186px;font-size:2.8px">© 2026 Lumo Care. All rights reserved.</div>
  </div>
</section>

<!-- ============ TREATMENT PAGE ============ -->
<section class="page treatment" style="left:360px;width:420px;height:1017px;background:var(--bg-page)">
  <div class="nav" style="height:19px">
    <div class="logo" style="left:51px;top:6px;font-size:5.5px">lumo.</div>
    <div class="nav-link active" style="left:141px;top:7px">Treatments</div>
    <div class="nav-link" style="left:171px;top:7px">How it Works</div>
    <div class="nav-link" style="left:204px;top:7px">About Us</div>
    <div class="nav-link" style="left:230px;top:7px">Contact</div>
    <div class="nav-link" style="left:320px;top:7px">Log In</div>
    <div class="pill-btn" style="left:339px;top:4px;width:33px;height:11px;font-size:3.4px">Get Started</div>
  </div>

  <div class="abs" style="left:48px;top:27px;background:#f6e6cf;color:var(--gold);font-size:2.8px;padding:2px 4px;border-radius:6px">Weight Loss Program</div>
  <h1 class="abs serif" style="left:48px;top:42px;width:205px;font-size:13px;line-height:1.22">Comprehensive GLP-1 Weight Loss Program</h1>
  <p class="abs small" style="left:48px;top:80px;width:200px;font-size:4.1px">A clinician-guided program featuring FDA-approved GLP-1 medications to help you lose weight sustainably and keep it off.</p>
  <div class="abs" style="left:53px;top:109px;font-size:3.4px;font-weight:600;color:var(--navy);display:flex;align-items:center;gap:3px">
    <svg width="5" height="5" viewBox="0 0 10 10"><path d="M5 1l3.5 1.4v2.8C8.5 7.3 7 8.6 5 9.2 3 8.6 1.5 7.3 1.5 5.2V2.4z" fill="none" stroke="#0B1B33" stroke-width=".9"/></svg>Reviewed by Lumo Medical Board</div>

  <div class="photo" role="img" aria-label="Colourful pills spilling from an orange prescription bottle on a blue background" style="left:48px;top:129px;width:198px;height:132px;background:radial-gradient(circle at 60% 50%,#7cc8f0,#52b0e8 70%)"></div>

  <div class="card" style="left:267px;top:26px;width:105px;height:142px;padding:11px 11px 0">
    <div style="display:flex;justify-content:space-between;align-items:center">
      <span class="serif" style="font-size:5.2px;font-weight:400">GLP-1 Program</span>
      <span style="font-size:2.8px;color:var(--gold)">★★★★★ <span style="color:var(--text)">(4.9)</span></span>
    </div>
    <div class="serif" style="font-size:11px;font-weight:400;margin-top:7px">$145<span style="font-family:var(--sans);font-size:3.2px;color:var(--muted)">/ month</span></div>
    <p class="small" style="font-size:2.8px;color:var(--muted);margin-top:4px">Pricing with insurance. Self-pay options available.</p>
    <div style="font-size:3.2px;color:var(--text);margin-top:8px;line-height:3.5">
      <div><span style="color:var(--gold)">✓</span>&nbsp; Medication included</div>
      <div><span style="color:var(--gold)">✓</span>&nbsp; Free shipping</div>
      <div><span style="color:var(--gold)">✓</span>&nbsp; Cancel anytime</div>
    </div>
    <div class="pill-btn" style="left:11px;top:106px;width:83px;height:15px;font-size:4px">Start Online Visit</div>
    <div style="position:absolute;left:0;right:0;top:127px;text-align:center;font-size:2.5px;color:var(--muted)">Secure &amp; HIPAA compliant</div>
  </div>

  <div class="abs serif" style="left:48px;top:285px;font-size:7px;color:#8d97a6">What it treats</div>
  <p class="abs small" style="left:48px;top:300px;width:198px;font-size:3.5px;color:#a6afbc">Our GLP-1 program is designed for adults dealing with obesity or overweight conditions who have struggled to lose weight through diet and exercise alone. It addresses the biological factors of weight retention by regulating appetite and improving metabolic function.</p>
  <div class="abs serif" style="left:48px;top:348px;font-size:7px;color:#8d97a6">How it works</div>
  <div class="abs serif" style="left:69px;top:366px;font-size:3.8px;color:#b7bfca">1. Medical Intake</div>
  <div class="abs" style="left:69px;top:374px;font-size:3px;color:#c2c9d3">Complete a quick medical questionnaire to see if you're a candidate.</div>

  <div class="abs serif" style="left:59px;top:451px;font-size:5.3px;font-weight:400">What's Included</div>
  <div class="abs" style="left:59px;top:463px;font-size:3.4px;color:var(--text);line-height:6.8px">
    <div>✓&nbsp;&nbsp;FDA-approved GLP-1 medication</div>
    <div>✓&nbsp;&nbsp;1-on-1 provider messaging</div>
    <div>✓&nbsp;&nbsp;Insurance concierges to help with coverage</div>
    <div>✓&nbsp;&nbsp;Free expedited shipping in discreet packaging</div>
  </div>

  <div class="abs serif" style="left:48px;top:532px;font-size:7px">Expected results timeline</div>
  <p class="abs small" style="left:48px;top:548px;width:200px;font-size:3.6px">Clinical trials have shown that patients taking GLP-1 medications alongside lifestyle changes lose on average 15% of their body weight over a year.</p>
  <div class="abs small" style="left:55px;top:569px;font-size:3.6px;line-height:10.7px">
    <div><b style="color:var(--navy)">Weeks 1-4:</b> Appetite reduction and early weight loss (often water weight).</div>
    <div><b style="color:var(--navy)">Months 2-3:</b> Steady, noticeable fat loss begins as dosage titrates up.</div>
    <div><b style="color:var(--navy)">Months 6+:</b> Significant body composition changes and metabolic improvements.</div>
  </div>

  <div class="card" style="left:48px;top:615px;width:198px;height:53px">
    <svg class="abs" style="left:9px;top:9px" width="6" height="6" viewBox="0 0 10 10"><path d="M5 1L9.3 8.8H.7z" fill="none" stroke="#E0A458" stroke-width=".9"/><path d="M5 4v2.3M5 7.3v.4" stroke="#E0A458" stroke-width=".9"/></svg>
    <div class="abs serif" style="left:21px;top:9px;font-size:4.4px;font-weight:400">Safety Information</div>
    <p class="abs small" style="left:21px;top:18px;width:168px;font-size:3.1px">GLP-1 medications are prescription-only. They are not appropriate for individuals with a personal or family history of medullary thyroid carcinoma or Multiple Endocrine Neoplasia syndrome type 2. Side effects may include nausea, vomiting, diarrhea, and constipation.</p>
  </div>
  <div class="card" style="left:48px;top:685px;width:198px;height:46px">
    <svg class="abs" style="left:9px;top:9px" width="6" height="6" viewBox="0 0 10 10"><circle cx="4" cy="3.3" r="2" fill="none" stroke="#E0A458" stroke-width=".8"/><path d="M.8 9c.4-2.2 1.7-3.2 3.2-3.2S6.8 6.8 7.2 9" fill="none" stroke="#E0A458" stroke-width=".8"/><path d="M6.8 4.8l1 1 1.6-1.8" fill="none" stroke="#E0A458" stroke-width=".8"/></svg>
    <div class="abs serif" style="left:21px;top:9px;font-size:4.4px;font-weight:400">Eligibility</div>
    <p class="abs small" style="left:21px;top:18px;width:168px;font-size:3.1px">This program is typically for adults with a BMI of 30 or greater, or a BMI of 27 or greater with a weight-related condition such as high blood pressure or type 2 diabetes.</p>
  </div>

  <div class="abs serif" style="left:48px;top:749px;font-size:7px">Frequently Asked Questions</div>
  <div class="faq-row" style="left:48px;top:769px;width:198px;height:23px;font-weight:500;font-size:4px">Am I eligible for this treatment?<span class="chev" style="border-color:var(--gold)"></span></div>
  <div class="faq-row" style="left:48px;top:792px;width:198px;height:23px;font-weight:500;font-size:4px">How quickly will I see results?<span class="chev" style="border-color:var(--gold)"></span></div>
  <div class="faq-row" style="left:48px;top:815px;width:198px;height:24px;font-weight:500;font-size:4px;border-bottom:1px solid var(--line)">What are the side effects?<span class="chev" style="border-color:var(--gold)"></span></div>

  <div class="abs" style="left:48px;top:860px;width:324px;height:1px;background:var(--line)"></div>
  <p class="abs" style="left:48px;top:867px;width:324px;font-size:2.3px;line-height:1.5;color:var(--muted)">* Disclaimer: The information provided is not a substitute for professional medical advice, diagnosis, or treatment. You should always consult your doctor or other qualified healthcare provider before starting any new treatment or stopping any existing treatment.</p>

  <div class="footer" style="top:903px;height:114px">
    <div class="f-logo" style="left:48px;top:23px;font-size:8px">lumo.</div>
    <div class="abs" style="left:48px;top:37px;width:75px;font-size:3.4px;line-height:1.6;color:#d3dbe7">Healthcare that fits your life. Prescription weight-loss and sexual-health treatments online.</div>
    <div class="f-head" style="left:175px;top:23px">TREATMENTS</div>
    <div class="f-link" style="left:175px;top:35px">Weight Loss</div>
    <div class="f-link" style="left:175px;top:46px">Sexual Health</div>
    <div class="f-link" style="left:175px;top:57px">Men's Health</div>
    <div class="f-head" style="left:245px;top:23px">COMPANY</div>
    <div class="f-link" style="left:245px;top:35px">About Us</div>
    <div class="f-link" style="left:245px;top:46px">How it Works</div>
    <div class="f-link" style="left:245px;top:57px">FAQ</div>
    <div class="f-link" style="left:245px;top:68px">Contact</div>
    <div class="f-head" style="left:315px;top:23px">LEGAL</div>
    <div class="f-link" style="left:315px;top:35px">Terms of Service</div>
    <div class="f-link" style="left:315px;top:46px">Privacy Policy</div>
    <div class="f-link" style="left:315px;top:57px">Telehealth Consent</div>
    <div class="f-link" style="left:315px;top:68px">Provider Login</div>
    <div class="f-rule" style="left:48px;width:324px;top:89px"></div>
    <div class="f-link" style="left:175px;top:98px;font-size:3px">© 2026 Lumo Care. All rights reserved.</div>
  </div>
</section>

<!-- ============ INTERIOR PAGE ============ -->
<section class="page interior" style="left:780px;width:420px;height:966px;background:var(--bg-page)">
  <div class="nav" style="height:19px">
    <div class="logo" style="left:50px;top:6px;font-size:5.5px">lumo.</div>
    <div class="nav-link" style="left:141px;top:7px">Treatments</div>
    <div class="nav-link active" style="left:171px;top:7px">How it Works</div>
    <div class="nav-link" style="left:204px;top:7px">About Us</div>
    <div class="nav-link" style="left:229px;top:7px">Contact</div>
    <div class="nav-link" style="left:320px;top:7px">Log In</div>
    <div class="pill-btn" style="left:339px;top:4px;width:33px;height:11px;font-size:3.4px">Get Started</div>
  </div>

  <div class="abs" role="img" aria-label="Faded lifestyle photo of a calm home interior" style="left:0;top:19px;width:420px;height:85px;background:linear-gradient(180deg,#c9ccd1,#dfe2e7 60%,var(--bg-page))"></div>
  <h1 class="abs serif" style="left:0;width:420px;top:30px;text-align:center;font-size:16px">How It Works</h1>
  <p class="abs small" style="left:130px;width:160px;top:58px;text-align:center;font-size:4px;color:#4f5d70">Simple. Private. Effective. Your journey to better health starts here.</p>

  <h2 class="abs serif" style="left:48px;top:195px;font-size:11px">1. Online Consultation</h2>
  <p class="abs small" style="left:48px;top:218px;width:150px;font-size:3.6px">Start by answering a few questions about your medical history, symptoms, and health goals. Our secure, <span style="color:var(--navy-2)">HIPAA-compliant</span> intake form takes less than 5 minutes to complete and can be done from anywhere, at any time.</p>
  <div class="photo" role="img" aria-label="Woman working on a laptop on a cream sofa beside a plant" style="left:220px;top:147px;width:152px;height:151px;background:linear-gradient(150deg,#e2d6c2,#c3ac8c 55%,#eee5d7);box-shadow:0 4px 12px rgba(11,27,51,.1)"></div>

  <div class="photo" role="img" aria-label="Smiling doctor in a white coat holding a tablet in a clinic" style="left:48px;top:347px;width:151px;height:145px;background:linear-gradient(160deg,#e6e1d8,#cfc6b7 50%,#f0ece5);box-shadow:0 4px 12px rgba(11,27,51,.1)"></div>
  <h2 class="abs serif" style="left:220px;top:389px;font-size:11px">2. Provider Review</h2>
  <p class="abs small" style="left:220px;top:411px;width:152px;font-size:3.6px">A U.S. licensed healthcare provider will carefully review your information. If they determine that our treatments are safe and appropriate for you, they will write a prescription. You can message your provider at any time if you have questions.</p>

  <h2 class="abs serif" style="left:48px;top:582px;font-size:11px">3. Free Discreet Delivery</h2>
  <p class="abs small" style="left:48px;top:604px;width:150px;font-size:3.6px">Your medication is shipped directly to your door in discreet, unbranded packaging. We offer free shipping on all orders and automatic refills so you never have to worry about running out of your medication.</p>
  <div class="photo" role="img" aria-label="Plain medication box resting on soft pink and mint fabric" style="left:220px;top:609px;width:152px;height:77px;background:linear-gradient(120deg,#efc3b3,#f4ddd3 55%,#dfeee8);border-radius:0 0 6px 6px"></div>

  <div class="card" style="left:50px;top:730px;width:320px;height:80px">
    <div class="pill-btn" style="left:148px;top:52px;width:24px;height:5px;font-size:2.4px;background:var(--navy-2)">Start Visit ↗</div>
  </div>

  <div class="footer" style="top:853px;height:113px">
    <div class="f-logo" style="left:48px;top:22px;font-size:8px">lumo.</div>
    <div class="abs" style="left:48px;top:37px;width:75px;font-size:3.4px;line-height:1.6;color:#d3dbe7">Healthcare that fits your life. Prescription weight-loss and sexual-health treatments online.</div>
    <div class="f-head" style="left:175px;top:21px">TREATMENTS</div>
    <div class="f-link" style="left:175px;top:33px">Weight Loss</div>
    <div class="f-link" style="left:175px;top:44px">Sexual Health</div>
    <div class="f-link" style="left:175px;top:55px">Men's Health</div>
    <div class="f-head" style="left:245px;top:21px">COMPANY</div>
    <div class="f-link" style="left:245px;top:33px">About Us</div>
    <div class="f-link" style="left:245px;top:44px">How it Works</div>
    <div class="f-link" style="left:245px;top:55px">FAQ</div>
    <div class="f-link" style="left:245px;top:66px">Contact</div>
    <div class="f-head" style="left:315px;top:21px">LEGAL</div>
    <div class="f-link" style="left:315px;top:33px">Terms of Service</div>
    <div class="f-link" style="left:315px;top:44px">Privacy Policy</div>
    <div class="f-link" style="left:315px;top:55px">Telehealth Consent</div>
    <div class="f-link" style="left:315px;top:66px">Provider Login</div>
    <div class="f-rule" style="left:48px;width:324px;top:90px"></div>
    <div class="f-link" style="left:175px;top:98px;font-size:3px">© 2026 Lumo Care. All rights reserved.</div>
  </div>
</section>

</body>
</html>
```